Corvel Traders logo

Corvel Traders is owned and operated by industry professionals with years of direct experience in providing customers with the right equipment to suit their needs. Our specialty lies within dealing in the Pellward Medical range of products. Our product range is suited to both the new user and for those that know what they want, a full line of products ranging from ultra-light wheelchairs, wheelchairs for sport and recreation and paediatric or just everyday use.

Industry/Entity Type

Recreation

Contact Information for Business Card

name, title, landline,fax,mobile,email,web address,physical address,logo,possibly a wheelchair pic

Requirements
Must have
• logo - uploaded
Nice to have
• colour scheme consistent with
www.corveltraders.com.au

```html
<!DOCTYPE html>
<html lang="en">
<head>
<meta charset="utf-8">
<title>Corvel Traders – Business Card</title>
<link href="https://fonts.googleapis.com/css2?family=Cabin:wght@400;600;700&family=Tenor+Sans&display=swap" rel="stylesheet">
<style>
  :root {
    --page-bg: #e4e4e6;
    --card-light: #eef0fb;
    --card-mid: #b3c0e8;
    --card-edge: #8599d3;
    --plum: #4a3049;
    --plum-soft: #6a4a6b;
    --ink: #141423;
    --logo-blue: #4f74b0;
    --chair-tone: rgba(110, 135, 200, 0.35);
  }
  * { margin: 0; padding: 0; box-sizing: border-box; }
  html, body {
    width: 1200px; height: 1000px; overflow: hidden;
    background: var(--page-bg);
  }
  .business-card {
    position: absolute; left: 100px; top: 213px;
    width: 1000px; height: 573px;
    background: radial-gradient(ellipse at 55% 42%, var(--card-light) 0%, var(--card-mid) 55%, var(--card-edge) 100%);
    box-shadow: 0 6px 18px rgba(0,0,0,0.25);
    overflow: hidden;
    font-family: "Cabin", "Trebuchet MS", sans-serif;
  }
  .chair-illustration {
    position: absolute; left: 490px; top: 40px;
    width: 440px; height: 460px;
    border-radius: 48% 40% 30% 30%;
    background: radial-gradient(ellipse at 60% 60%, var(--chair-tone) 0%, rgba(110,135,200,0.12) 60%, rgba(110,135,200,0) 80%);
  }
  .brand-mark {
    position: absolute; left: 90px; top: 190px;
    display: flex; align-items: center; gap: 18px;
  }
  .brand-dot {
    width: 70px; height: 70px; border-radius: 50%;
    background: var(--logo-blue);
  }
  .brand-name {
    font-family: "Cabin", "Trebuchet MS", sans-serif;
    font-weight: 700; font-size: 52px; color: var(--plum-soft);
    line-height: 1.05;
  }
  .holder {
    position: absolute; left: 555px; top: 112px; width: 400px;
    text-align: center; color: var(--ink);
    font-family: "Tenor Sans", "Optima", sans-serif;
  }
  .holder-name { font-size: 42px; line-height: 1; }
  .holder-title { font-size: 16px; letter-spacing: 2.5px; margin-top: 4px; }
  .divider { position: absolute; left: 0; top: 0; }
  .address-block {
    position: absolute; left: 55px; top: 405px;
    color: var(--ink); font-size: 25px; line-height: 36px;
  }
  .address-block .street { font-weight: 700; }
  .address-block .web, .address-block .email { letter-spacing: 0.6px; }
  .phone-list {
    position: absolute; right: 60px; top: 405px;
    list-style: none; color: var(--ink);
    font-size: 27px; line-height: 36px; letter-spacing: 0.5px;
  }
  .phone-list li { display: flex; align-items: center; gap: 12px; }
  .phone-list svg { width: 24px; height: 24px; fill: var(--plum); }
</style>
</head>
<body>
  <div class="business-card">
    <div class="chair-illustration" role="img" aria-label="Faint wheelchair illustration"></div>

    <div class="brand-mark">
      <span class="brand-dot"></span>
      <span class="brand-name">Corvel<br>Traders</span>
    </div>

    <div class="holder">
      <div class="holder-name">Corvel Traders</div>
      <div class="holder-title">MANAGER</div>
    </div>

    <svg class="divider" width="1000" height="573" aria-hidden="true">
      <polyline points="55,525 567,525 567,400 940,400" fill="none" stroke="var(--plum)" stroke-width="3"/>
    </svg>

    <div class="address-block">
      <div class="street">Unit 8 14 Fernlea Road, HALLOWAY</div>
      <div class="email">info@corveltraders.com.au</div>
      <div class="web">www.corveltraders.com.au</div>
    </div>

    <ul class="phone-list">
      <li>
        <svg viewBox="0 0 24 24" aria-label="Mobile"><path d="M7 1h10a1 1 0 0 1 1 1v20a1 1 0 0 1-1 1H7a1 1 0 0 1-1-1V2a1 1 0 0 1 1-1zm1 3v9h8V4zm1 11v2h2v-2zm4 0v2h2v-2zm-4 3v2h2v-2zm4 0v2h2v-2z"/></svg>
        +61 400 555 018
      </li>
      <li>
        <svg viewBox="0 0 24 24" aria-label="Phone"><path d="M2 8c0-3 4-5 10-5s10 2 10 5v2h-5V8c-1-1-3-1.4-5-1.4S8 7 7 8v2H2zm4 3h12l3 9H3zm6 2a3 3 0 1 0 0 6 3 3 0 0 0 0-6z"/></svg>
        +61 2 5550 1142
      </li>
      <li>
        <svg viewBox="0 0 24 24" aria-label="Fax"><path d="M7 2h9v6H7zm-4 7h18v12H3zm3 3v2h4v-2zm0 4v2h4v-2zm7-4v2h5v-2zm0 4v2h5v-2z"/></svg>
        +61 2 5550 1176
      </li>
    </ul>
  </div>
</body>
</html>
```